Hairdressing Salon called; Velvet Tress. Style Lives Here

Velvet Tress
We Love Hair
418 Penrose Lane Birch Vale
5183742
Business card not to fussy.
I would like it to be a Black background with White and/or Grey lettering.

I really like the business card attached, so if the front looked like this I would be really happy, but would also like my address and phone number on the front.

On the back I would like two options of
1: reward card; buy any Haircare product over $20 on any visit and on the tenth product receive a complimentry Treatment and
2: appointment times and date

Industry/Entity Type

Business

Contact Information for Business Card

Velvet Tress
We Love Hair
5183742
418 Penrose Lane, Birch Vale
This must all be included on the front of the card

Font styles to use
Serif
Decorative
Script

Colors
1b1b1b
757575
ffffff

Requirements
Must have
• My phone number and address
Should not have
• Pictures on the front

```html
<!DOCTYPE html>
<html lang="en">
<head>
<meta charset="utf-8">
<title>Velvet Tress – Business Card</title>
<link rel="stylesheet" href="https://fonts.googleapis.com/css2?family=Rouge+Script&display=swap">
<style>
  :root {
    --card-black: #1b1b1b;
    --ink-white: #ffffff;
    --ink-grey: #757575;
    --page: #ffffff;
  }
  html, body {
    margin: 0;
    padding: 0;
    width: 1200px;
    height: 1001px;
    overflow: hidden;
    background: var(--page);
  }
  .canvas {
    position: relative;
    width: 1200px;
    height: 1001px;
    font-family: "Rouge Script", cursive;
  }
  .card {
    position: absolute;
    width: 657px;
    height: 449px;
    background: var(--card-black);
  }
  .card--front { left: 0; top: 0; }
  .card--back { left: 543px; top: 552px; }

  .headline {
    position: absolute;
    left: 122px;
    top: 160px;
    margin: 0;
    font-weight: 400;
    font-size: 48px;
    line-height: 1;
    white-space: nowrap;
    letter-spacing: 0.5px;
  }
  .ink-white { color: var(--ink-white); }
  .ink-grey { color: var(--ink-grey); }

  .contact {
    position: absolute;
    left: 331px;
    top: 330px;
    width: 270px;
    margin: 0;
    color: var(--ink-white);
    font-size: 26px;
    line-height: 38px;
    font-style: normal;
    text-align: center;
    letter-spacing: 0.5px;
  }
  .contact__phone { letter-spacing: 2px; }

  .reward {
    position: absolute;
    left: 58px;
    top: 64px;
    margin: 0;
    color: var(--ink-grey);
    font-size: 29px;
    line-height: 45px;
  }
  .reward p { margin: 0; }
  .appointment {
    position: absolute;
    left: 58px;
    top: 290px;
    margin: 0;
    color: var(--ink-grey);
    font-size: 29px;
    line-height: 45px;
  }
</style>
</head>
<body>
<main class="canvas">
  <section class="card card--front" aria-label="Card front">
    <h1 class="headline"><span class="ink-white">Velvet Tress.</span> <span class="ink-white">Style Lives</span> <span class="ink-grey">Here</span></h1>
    <address class="contact">
      <div class="contact__address">418 Penrose Lane Birch Vale</div>
      <div class="contact__phone">5183742</div>
    </address>
  </section>

  <section class="card card--back" aria-label="Card back">
    <div class="reward">
      <p class="reward__title">Reward Card</p>
      <p>Buy any haircare product over 20</p>
      <p>ony any visit and on the tenth product receive a</p>
      <p>complimentry Treatment</p>
    </div>
    <p class="appointment">Appoitment times and date:</p>
  </section>
</main>
</body>
</html>
```